Business card design and logo for plumbing bussiness

We are wanting a logo for a plumbing business is Queensland Australia. KLV Plumbing and Drainage will be doing works on domestic and commercial sites.
Plumbing, drainage and gas works. We are wanting something that will stand out and be noticed. Colours could be black blue and white but open for suggestions.

Target Market(s)

Builders and home renovators

Industry/Entity Type

Plumbing

Contact Information for Business Card

Dorian Machell - Director
0417 582 031
dorian@klvplumbing-example.com.au
QBCC: 374 8106
ABN: 52 913 207 615

Font styles to use
Sans Serif

Colors
000000

Requirements
Must have
• Clear defined branding

```html
<!DOCTYPE html>
<html lang="en">
<head>
<meta charset="utf-8">
<title>KLV Plumbing and Drainage – Business Card</title>
<link rel="stylesheet" href="https://fonts.googleapis.com/css2?family=Raleway:wght@500;600&display=swap">
<style>
  :root {
    --card-bg: #2b2a2f;
    --brand-blue: #22536f;
    --brand-blue-shade: #1d4359;
    --ink-dark: #2b2a2f;
  }
  html, body {
    margin: 0;
    padding: 0;
    width: 1200px;
    height: 750px;
    overflow: hidden;
    background: var(--card-bg);
  }
  .business-card {
    display: block;
    width: 1200px;
    height: 750px;
    background: var(--card-bg);
  }
  .card-text {
    font-family: "Raleway", Arial, sans-serif;
  }
  .brand-dot { fill: var(--brand-blue); }
  .brand-name,
  .brand-trade {
    fill: var(--brand-blue);
    font-weight: 600;
  }
  .brand-name {
    font-size: 84px;
    letter-spacing: 3px;
  }
  .brand-trade {
    font-size: 26px;
    letter-spacing: 4px;
  }
  .ribbon-back { fill: var(--brand-blue-shade); }
  .ribbon-line { fill: var(--brand-blue-shade); }
  .ribbon-front { fill: var(--brand-blue); }
  .tagline {
    fill: var(--ink-dark);
    font-size: 44px;
    font-weight: 600;
  }
  .contact-role,
  .contact-name {
    fill: var(--brand-blue);
    font-size: 40px;
    font-weight: 500;
    letter-spacing: 1px;
  }
  .contact-detail {
    fill: var(--brand-blue);
    font-size: 20px;
    font-weight: 500;
    letter-spacing: 0.5px;
  }
</style>
</head>
<body>
<svg class="business-card" viewBox="0 0 1200 750" xmlns="http://www.w3.org/2000/svg" aria-label="KLV Plumbing and Drainage business card">
  <g class="brand">
    <circle class="brand-dot" cx="513" cy="214" r="24"/>
    <text class="card-text brand-name" x="627" y="244" text-anchor="middle">KLV</text>
    <text class="card-text brand-trade" x="600" y="300" text-anchor="middle">PLUMBING AND DRAINAGE</text>
  </g>

  <g class="ribbon">
    <polygon class="ribbon-back" points="372,408 850,408 870,514 350,514"/>
    <rect class="ribbon-line" x="0" y="514" width="1200" height="16"/>
    <polygon class="ribbon-front" points="372,408 850,408 794,576 429,576"/>
    <text class="card-text tagline" x="611" y="466" text-anchor="middle">Builders and home</text>
    <text class="card-text tagline" x="611" y="526" text-anchor="middle">renovators</text>
  </g>

  <g class="contact-details">
    <text class="card-text contact-detail" x="40" y="604">0417 582 031</text>
    <text class="card-text contact-detail" x="40" y="634">dorian@klvplumbing-example.com.au</text>
    <text class="card-text contact-detail" x="40" y="664">QBCC: 374 8106</text>
    <text class="card-text contact-detail" x="40" y="694">ABN: 52 913 207 615</text>
  </g>

  <g class="contact">
    <text class="card-text contact-role" x="1045" y="618" text-anchor="middle">Director</text>
    <text class="card-text contact-name" x="1170" y="674" text-anchor="end">Dorian Machell</text>
  </g>
</svg>
</body>
</html>
```